Create website for home automation - Control your lighting, fans, blinds etc remotely by smartphone

Plan for STOREVAN Website - Brightnest Dwellings
Company name: Brightnest Dwellings
Company Slogan: Calm Evenings Done Right
Clean, Modern, Easy to Navigate, easy to maintain - not a lot of coding. We need flash technology but displaying simply what we do.
What we provide:
We will be offering wireless switch which can be added to iOS/Android App via WiFi, allowing users to remotely turn on/off connected lights, fans, security cameras, appliances, irrigation, humidifier separately from anywhere at any time.
Control your home away from home. No more wandering of your mind on those lights or appliances which you might have left switched on. No need to drive back home to check and switch them off. Save that energy, money and time just with a click of your phone no matter how far you are from home.
Replace your home electrical switches with smart switches. They retrofit existing electrical switches and allow you to make the transformation as needed.
Easy to use and intuitive app allows you to control your lights and devices just at a click. Set any kind of ambiance suiting your occasion.
Set scenes in smartphone app to group and operate your devices just at a button click. Same device can be included in more than one scene.
Collections and Products
Light Switches
Wall Plugs
Fan Switch
Pendants etc special lighting types.
Light Dimmers
Blind Controllers
Home Page:
Home page needs to telling customers what we do and how we do it in a few words to grab people.
Logo
Phone
Email
Support – Download instructions per product
Client login
Wholesale login
Promotional video to be on home screen - this is a short 1.5 - 2 min illustration introduction video to who we are and what we do - this is yet to be created)
Social media link - Chatterly
Pages:
FAQ
About Us
Support/Shipping/Returns policy
Support/Installation
Blog posts
Product pages:
Description
Price
Space for where a video will be featured - how each product works/installation.
Reviews
Our competition:
http://www.pvorn.com.au
https://lumalodgeguide.com.au/2018/04/05/best-smart-light-switches-and-plugs/
https://www.zentiqo.com
Attachments:
Logo
Product pics
Promotional video - if ready

```html
<!DOCTYPE html>
<html lang="en">
<head>
<meta charset="utf-8">
<title>Blogs – Brightnest Dwellings</title>
<link href="https://fonts.googleapis.com/css2?family=Oswald:wght@300;400;500;700&family=Tinos:wght@400;700&display=swap" rel="stylesheet">
<style>
  :root {
    --navy: #0e3573;
    --blue: #0f73b8;
    --green: #3dba74;
    --white: #ffffff;
    --wood-dark: #3e2516;
    --wood-mid: #7a4f31;
    --wood-light: #a47550;
    --ink: #111111;
    --photo-a: #6b4a2a;
    --photo-b: #b08a60;
  }
  * { box-sizing: border-box; margin: 0; padding: 0; }
  html, body { width: 1200px; height: 2400px; overflow: hidden; background: var(--white); }
  body { position: relative; font-family: "Oswald", sans-serif; color: var(--white); }

  .hero {
    position: absolute; left: 0; top: 0; width: 1200px; height: 395px;
    background: linear-gradient(160deg, var(--wood-light) 0%, var(--wood-mid) 45%, var(--wood-dark) 100%);
  }
  .brand {
    position: absolute; left: 149px; top: 4px; width: 148px;
    display: flex; flex-direction: column; align-items: center; gap: 6px;
    font-family: "Oswald", sans-serif; font-weight: 500; font-size: 13px; line-height: 1; color: var(--navy);
    white-space: nowrap;
  }
  .brand-mark { width: 26px; height: 26px; background: var(--navy); }
  .main-nav { position: absolute; top: 6px; left: 0; }
  .main-nav a {
    position: absolute; top: 0; color: var(--white); text-decoration: none;
    font-weight: 400; font-size: 21px; white-space: nowrap; letter-spacing: -0.4px;
  }
  .main-nav a.active { font-weight: 500; font-size: 21px; top: -1px; letter-spacing: -0.6px; }
  .main-nav a.active::after {
    content: ""; position: absolute; left: 6px; right: 6px; bottom: -5px; height: 3px; background: var(--green);
  }
  .social {
    position: absolute; top: 12px; left: 798px; width: 146px; display: flex; gap: 6px;
    white-space: nowrap;
  }
  .social span { font-size: 12px; font-weight: 500; color: var(--white); }
  .login {
    position: absolute; left: 952px; top: 6px; width: 96px; height: 29px; background: var(--green);
    color: var(--white); font-weight: 500; font-size: 20px; text-align: center; line-height: 29px; text-decoration: none;
  }
  .page-title {
    position: absolute; left: 459px; top: 62px; font-weight: 700; font-size: 56px; color: var(--white);
  }

  .blog-grid { position: absolute; left: 0; top: 0; }
  .post {
    position: absolute; width: 264px; height: 403px; background: var(--navy);
    font-family: "Tinos", serif; text-align: center;
  }
  .post.alt { background: var(--blue); }
  .post-photo { width: 264px; height: 150px; background: linear-gradient(135deg, var(--photo-a), var(--photo-b)); }
  .post-title { margin-top: 16px; font-weight: 700; font-size: 21px; line-height: 1.2; white-space: nowrap; }
  .post-excerpt {
    margin: 4px 0 0 38px; width: 186px; text-align: left; font-size: 14px; line-height: 15px;
  }
  .read-more {
    position: absolute; left: 66px; top: 333px; width: 138px; height: 53px; background: var(--green);
    color: var(--white); font-size: 20px; line-height: 53px; text-decoration: none;
  }

  .site-footer { position: absolute; left: 0; top: 2216px; width: 1200px; height: 184px; background: var(--blue); }
  .footer-nav a {
    position: absolute; top: 20px; color: var(--white); text-decoration: none; font-weight: 500; font-size: 14px; white-space: nowrap;
  }
  .follow { position: absolute; left: 637px; top: 18px; font-weight: 500; font-size: 17px; }
  .footer-social {
    position: absolute; left: 604px; top: 44px; display: flex; gap: 5px; font-size: 10.5px; font-weight: 500; white-space: nowrap;
  }
  .store-badge { position: absolute; left: 618px; width: 97px; height: 29px; background: var(--ink); border: 1px solid #777; border-radius: 4px; }
  .contact-form label {
    position: absolute; background: var(--white); color: var(--ink); font-size: 17px; font-weight: 500; padding-left: 4px; line-height: 24px;
  }
  .submit {
    position: absolute; left: 965px; top: 150px; width: 96px; height: 28px; border-radius: 14px; background: var(--green);
    color: var(--white); font-weight: 700; font-size: 19px; text-align: center; line-height: 28px;
  }
</style>
</head>
<body>
  <header class="hero" role="img" aria-label="Photo of hands typing on a laptop on a wooden desk with flowers, coffee cup and phone">
    <div class="brand"><span class="brand-mark"></span>Brightnest Dwellings</div>
    <nav class="main-nav">
      <a href="#" style="left:312px">Home</a>
      <a href="#" style="left:376px">FAQ</a>
      <a href="#" style="left:428px">About Us</a>
      <a href="#" style="left:515px">Support</a>
      <a href="#" class="active" style="left:593px">Installation</a>
      <a href="#" style="left:696px">Blog</a>
    </nav>
    <div class="social"><span>Chatterly</span><span>Peeplo</span><span>Snapgrid</span></div>
    <a href="#" class="login">Login</a>
    <h1 class="page-title">Blogs</h1>
  </header>

  <main class="blog-grid">
    <article class="post" style="left:149px;top:445px"><div class="post-photo" role="img" aria-label="Man using a smartphone outdoors"></div><h2 class="post-title">Automating Your Home</h2><p class="post-excerpt">Lorem ipsum dolor sit amet, consectetur adipiscing elit, sed do eiusmod tempor incididunt ut labore et dolore magna aliqua. Ut enim ad minim veniam, quis nostrud exercitation.</p><a href="#" class="read-more">Read More</a></article>
    <article class="post alt" style="left:466px;top:445px"><div class="post-photo" role="img" aria-label="Person working on a laptop with charts"></div><h2 class="post-title">Automating Your Home</h2><p class="post-excerpt">Lorem ipsum dolor sit amet, consectetur adipiscing elit, sed do eiusmod tempor incididunt ut labore et dolore magna aliqua. Ut enim ad minim veniam, quis nostrud exercitation.</p><a href="#" class="read-more">Read More</a></article>
    <article class="post" style="left:781px;top:445px"><div class="post-photo" role="img" aria-label="House keys with a small house keyring on a table"></div><h2 class="post-title">Automating Your Home</h2><p class="post-excerpt">Lorem ipsum dolor sit amet, consectetur adipiscing elit, sed do eiusmod tempor incididunt ut labore et dolore magna aliqua. Ut enim ad minim veniam, quis nostrud exercitation.</p><a href="#" class="read-more">Read More</a></article>

    <article class="post" style="left:149px;top:875px"><div class="post-photo" role="img" aria-label="Man using a smartphone outdoors"></div><h2 class="post-title">Automating Your Home</h2><p class="post-excerpt">Lorem ipsum dolor sit amet, consectetur adipiscing elit, sed do eiusmod tempor incididunt ut labore et dolore magna aliqua. Ut enim ad minim veniam, quis nostrud exercitation.</p><a href="#" class="read-more">Read More</a></article>
    <article class="post alt" style="left:466px;top:875px"><div class="post-photo" role="img" aria-label="Person working on a laptop with charts"></div><h2 class="post-title">Automating Your Home</h2><p class="post-excerpt">Lorem ipsum dolor sit amet, consectetur adipiscing elit, sed do eiusmod tempor incididunt ut labore et dolore magna aliqua. Ut enim ad minim veniam, quis nostrud exercitation.</p><a href="#" class="read-more">Read More</a></article>
    <article class="post" style="left:781px;top:875px"><div class="post-photo" role="img" aria-label="House keys with a small house keyring on a table"></div><h2 class="post-title">Automating Your Home</h2><p class="post-excerpt">Lorem ipsum dolor sit amet, consectetur adipiscing elit, sed do eiusmod tempor incididunt ut labore et dolore magna aliqua. Ut enim ad minim veniam, quis nostrud exercitation.</p><a href="#" class="read-more">Read More</a></article>

    <article class="post" style="left:149px;top:1304px"><div class="post-photo" role="img" aria-label="Man using a smartphone outdoors"></div><h2 class="post-title">Automating Your Home</h2><p class="post-excerpt">Lorem ipsum dolor sit amet, consectetur adipiscing elit, sed do eiusmod tempor incididunt ut labore et dolore magna aliqua. Ut enim ad minim veniam, quis nostrud exercitation.</p><a href="#" class="read-more">Read More</a></article>
    <article class="post alt" style="left:466px;top:1304px"><div class="post-photo" role="img" aria-label="Person working on a laptop with charts"></div><h2 class="post-title">Automating Your Home</h2><p class="post-excerpt">Lorem ipsum dolor sit amet, consectetur adipiscing elit, sed do eiusmod tempor incididunt ut labore et dolore magna aliqua. Ut enim ad minim veniam, quis nostrud exercitation.</p><a href="#" class="read-more">Read More</a></article>
    <article class="post" style="left:781px;top:1304px"><div class="post-photo" role="img" aria-label="House keys with a small house keyring on a table"></div><h2 class="post-title">Automating Your Home</h2><p class="post-excerpt">Lorem ipsum dolor sit amet, consectetur adipiscing elit, sed do eiusmod tempor incididunt ut labore et dolore magna aliqua. Ut enim ad minim veniam, quis nostrud exercitation.</p><a href="#" class="read-more">Read More</a></article>

    <article class="post" style="left:149px;top:1742px"><div class="post-photo" role="img" aria-label="Man using a smartphone outdoors"></div><h2 class="post-title">Automating Your Home</h2><p class="post-excerpt">Lorem ipsum dolor sit amet, consectetur adipiscing elit, sed do eiusmod tempor incididunt ut labore et dolore magna aliqua. Ut enim ad minim veniam, quis nostrud exercitation.</p><a href="#" class="read-more">Read More</a></article>
    <article class="post alt" style="left:466px;top:1742px"><div class="post-photo" role="img" aria-label="Person working on a laptop with charts"></div><h2 class="post-title">Automating Your Home</h2><p class="post-excerpt">Lorem ipsum dolor sit amet, consectetur adipiscing elit, sed do eiusmod tempor incididunt ut labore et dolore magna aliqua. Ut enim ad minim veniam, quis nostrud exercitation.</p><a href="#" class="read-more">Read More</a></article>
    <article class="post" style="left:781px;top:1742px"><div class="post-photo" role="img" aria-label="House keys with a small house keyring on a table"></div><h2 class="post-title">Automating Your Home</h2><p class="post-excerpt">Lorem ipsum dolor sit amet, consectetur adipiscing elit, sed do eiusmod tempor incididunt ut labore et dolore magna aliqua. Ut enim ad minim veniam, quis nostrud exercitation.</p><a href="#" class="read-more">Read More</a></article>
  </main>

  <footer class="site-footer">
    <nav class="footer-nav">
      <a href="#" style="left:141px">Home</a>
      <a href="#" style="left:214px">About Us</a>
      <a href="#" style="left:306px">Products</a>
      <a href="#" style="left:395px">Design</a>
      <a href="#" style="left:474px">Services</a>
      <a href="#" style="left:558px">Contact Us</a>
    </nav>
    <div class="follow">Follow</div>
    <div class="footer-social"><span>Chatterly</span><span>Peeplo</span><span>Snapgrid</span></div>
    <div class="store-badge" style="top:72px"></div>
    <div class="store-badge" style="top:104px"></div>
    <form class="contact-form">
      <label style="left:733px;top:3px;width:157px;height:26px">Name:</label>
      <label style="left:909px;top:3px;width:157px;height:26px">Phone:</label>
      <label style="left:733px;top:38px;width:333px;height:26px">Email</label>
      <label style="left:733px;top:70px;width:333px;height:76px">Message:</label>
      <div class="submit">Submit</div>
    </form>
  </footer>
</body>
</html>
```